Artist/Artwork Product Catalog

I need a small brief product catalog to display my art for purchase to my interior designer clients, to purchase for their clients. Should be 5 - 10 pages with art/canvas display mock up pictures. Sections should include About the artist, space for pricing and art titles, Editable Section Names (3 sections-not including previously mentioned sections), Contact info-including social media. I would like modern and simplistic. My art is filled with bright colors and as such want the design of the catalog to be black and white so as not to detract from the art itself. Please refer to my website and instagram for further design resource: www.torevandrelle.com ; @vandrelletor (instagram)
Target Market(s)
Interior Designers, Collectors, Galleries
Industry/Entity Type
Art Gallery
Font styles to use
Colors
Designer to choose colors to be used in the design.
Requirements
Must have
- Must have my artwork included in catalog displayed in canvas wall art mock up. Will send files upon acceptance of catalog design. Need to be printer ready upon project completion as well as editable for future changes as needed. Would like a smaller sized catalog, maybe A4.
Nice to have
- Editable for future use. Would love to have new logo integrated into catalog.
Should not have
- No distracting colors or ornate decorative design

```html
<!DOCTYPE html>
<html lang="en">
<head>
<meta charset="utf-8">
<title>Eyes – Art Catalog Page</title>
<link rel="stylesheet" href="https://fonts.googleapis.com/css2?family=Open+Sans:wght@300;400&display=swap">
<style>
  :root {
    --backdrop: #f2f2f2;
    --page: #232323;
    --ink: #ffffff;
    --ink-soft: #e6e6e6;
    --accent: #e0701f;
    --rule: #4a4a4a;
    --frame: #f5f5f5;
  }
  * { box-sizing: border-box; margin: 0; padding: 0; }
  html, body {
    width: 1200px; height: 1200px; overflow: hidden;
    background: var(--backdrop);
    font-family: "Open Sans", Arial, sans-serif;
  }
  .catalog-page {
    position: absolute; left: 138px; top: 24px;
    width: 924px; height: 1151px;
    background: var(--page); color: var(--ink);
  }
  .page-header {
    position: absolute; left: 32px; top: 42px; width: 861px; height: 67px;
    border-bottom: 2px solid var(--ink);
  }
  .header-band {
    position: absolute; left: 0; top: 0; width: 640px; height: 65px;
    background: linear-gradient(90deg, #e21fc6 0%, #f4e9f6 18%, #c9c9c9 32%, #ee1fa8 48%, #b9b9b9 62%, #9a2a9a 80%, var(--page) 100%);
  }
  .page-title {
    position: absolute; right: 20px; top: 2px;
    font-weight: 300; font-size: 48px; line-height: 60px; letter-spacing: 1px;
  }
  .intro {
    position: absolute; left: 32px; top: 131px; width: 861px;
    font-size: 17px; line-height: 24.5px; text-align: justify; color: var(--ink-soft);
  }
  .divider-v {
    position: absolute; left: 460px; top: 259px; width: 4px; height: 861px; background: var(--rule);
  }
  .divider-h {
    position: absolute; left: 32px; top: 687px; width: 861px; height: 4px; background: var(--rule);
  }
  .artwork-card { position: absolute; width: 416px; }
  .card-title { font-weight: 400; font-size: 24px; line-height: 30px; height: 43px; }
  .card-body { display: flex; gap: 15px; }
  .artwork-frame {
    width: 276px; height: 280px; flex: none;
    border: 2px solid var(--frame); padding: 12px;
  }
  .artwork-fill { width: 100%; height: 100%; }
  .fill-orange { background: radial-gradient(circle at 40% 40%, #ffffff 0%, #f25a1e 45%, #e21b1b 75%, #ff8a1c 100%); }
  .fill-blue { background: radial-gradient(circle at 40% 40%, #ffffff 0%, #35b7f0 40%, #4a2fd1 75%, #7a4be8 100%); }
  .fill-green { background: radial-gradient(circle at 40% 40%, #ffffff 0%, #2fbf2a 45%, #128a16 80%, #d9d9d9 100%); }
  .fill-pink { background: radial-gradient(circle at 40% 40%, #ffffff 0%, #ff2fd0 45%, #e0136a 80%, #f7c2ee 100%); }
  .card-notes { width: 125px; font-size: 12.5px; line-height: 15.4px; text-align: justify; color: var(--ink-soft); }
  .label { color: var(--accent); text-transform: uppercase; text-align: left; }
  .card-notes p + .label { margin-top: 11px; }
  .card-foot { display: flex; justify-content: space-between; margin-top: 8px; }
  .foot-text { width: 279px; font-size: 12.5px; line-height: 15.4px; text-align: justify; color: var(--ink-soft); }
  .price { text-align: right; padding-top: 10px; }
  .price-label { color: var(--accent); font-weight: 300; font-size: 24px; line-height: 30px; }
  .price-value { font-weight: 300; font-size: 28px; line-height: 34px; }
</style>
</head>
<body>
<main class="catalog-page">
  <header class="page-header">
    <div class="header-band" role="img" aria-label="Cropped detail of the Eyes artwork in magenta, white and grey"></div>
    <h1 class="page-title">EYES</h1>
  </header>
  <p class="intro">Proin facilisis elit vitae mollis faucibus. Proin vitae massa nec mauris dictum consequat. Maecenas congue non felis a malesuada. Phasellus ullamcorper laoreet felis eu viverra. In at tincidunt tortor. Praesent tempor eros vitae elit dignissim, vitae elementum dui dapibus. Duis tristique, ligula eget lobortis accumsan, nibh enim venenatis urna, a commodo elit ex ac urna.</p>

  <div class="divider-v"></div>
  <div class="divider-h"></div>

  <article class="artwork-card" style="left:32px; top:261px;">
    <h2 class="card-title">Tittle EYES 01</h2>
    <div class="card-body">
      <div class="artwork-frame"><div class="artwork-fill fill-orange" role="img" aria-label="Artwork Eyes 01: red and orange ovals on white"></div></div>
      <div class="card-notes">
        <h3 class="label">About Art</h3>
        <p>Proin facilisis elit vitae mollis faucibus. Proin vitae massa nec mauris dictum consequat. Maecenas congue non felis a malesuada. Phasellus ullamcorper laoreet felis eu viverra.</p>
        <h3 class="label">About Artist</h3>
        <p>Proin facilisis elit vitae mollis faucibus. Proin vitae massa nec mauris dictum consequat.</p>
      </div>
    </div>
    <div class="card-foot">
      <div class="foot-text"><h3 class="label" style="text-transform:none;font-weight:400;">Secition 03 and 04</h3><p>Proin facilisis elit vitae mollis faucibus. Proin vitae massa nec mauris dictum consequat. Maecenas congue non felis a malesuada. Phasellus ullamcorper laoreet felis eu viverra.</p></div>
      <div class="price"><div class="price-label">Price:</div><div class="price-value">650$</div></div>
    </div>
  </article>

  <article class="artwork-card" style="left:476px; top:261px;">
    <h2 class="card-title">Tittle EYES 02</h2>
    <div class="card-body">
      <div class="artwork-frame"><div class="artwork-fill fill-blue" role="img" aria-label="Artwork Eyes 02: blue and cyan ovals on violet"></div></div>
      <div class="card-notes">
        <h3 class="label">About Art</h3>
        <p>Proin facilisis elit vitae mollis faucibus. Proin vitae massa nec mauris dictum consequat. Maecenas congue non felis a malesuada. Phasellus ullamcorper laoreet felis eu viverra.</p>
        <h3 class="label">About Artist</h3>
        <p>Proin facilisis elit vitae mollis faucibus. Proin vitae massa nec mauris dictum consequat.</p>
      </div>
    </div>
    <div class="card-foot">
      <div class="foot-text"><h3 class="label" style="text-transform:none;font-weight:400;">Secition 03 and 04</h3><p>Proin facilisis elit vitae mollis faucibus. Proin vitae massa nec mauris dictum consequat. Maecenas congue non felis a malesuada. Phasellus ullamcorper laoreet felis eu viverra.</p></div>
      <div class="price"><div class="price-label">Price:</div><div class="price-value">650$</div></div>
    </div>
  </article>

  <article class="artwork-card" style="left:32px; top:694px;">
    <h2 class="card-title">Tittle EYES 03</h2>
    <div class="card-body">
      <div class="artwork-frame"><div class="artwork-fill fill-green" role="img" aria-label="Artwork Eyes 03: green ovals on white"></div></div>
      <div class="card-notes">
        <h3 class="label">About Art</h3>
        <p>Proin facilisis elit vitae mollis faucibus. Proin vitae massa nec mauris dictum consequat. Maecenas congue non felis a malesuada. Phasellus ullamcorper laoreet felis eu viverra.</p>
        <h3 class="label">About Artist</h3>
        <p>Proin facilisis elit vitae mollis faucibus. Proin vitae massa nec mauris dictum consequat.</p>
      </div>
    </div>
    <div class="card-foot">
      <div class="foot-text"><h3 class="label" style="text-transform:none;font-weight:400;">Secition 03 and 04</h3><p>Proin facilisis elit vitae mollis faucibus. Proin vitae massa nec mauris dictum consequat. Maecenas congue non felis a malesuada. Phasellus ullamcorper laoreet felis eu viverra.</p></div>
      <div class="price"><div class="price-label">Price:</div><div class="price-value">650$</div></div>
    </div>
  </article>

  <article class="artwork-card" style="left:476px; top:694px;">
    <h2 class="card-title">Tittle EYES 04</h2>
    <div class="card-body">
      <div class="artwork-frame"><div class="artwork-fill fill-pink" role="img" aria-label="Artwork Eyes 04: magenta and pink ovals on white"></div></div>
      <div class="card-notes">
        <h3 class="label">About Art</h3>
        <p>Proin facilisis elit vitae mollis faucibus. Proin vitae massa nec mauris dictum consequat. Maecenas congue non felis a malesuada. Phasellus ullamcorper laoreet felis eu viverra.</p>
        <h3 class="label">About Artist</h3>
        <p>Proin facilisis elit vitae mollis faucibus. Proin vitae massa nec mauris dictum consequat.</p>
      </div>
    </div>
    <div class="card-foot">
      <div class="foot-text"><h3 class="label" style="text-transform:none;font-weight:400;">Secition 03 and 04</h3><p>Proin facilisis elit vitae mollis faucibus. Proin vitae massa nec mauris dictum consequat. Maecenas congue non felis a malesuada. Phasellus ullamcorper laoreet felis eu viverra.</p></div>
      <div class="price"><div class="price-label">Price:</div><div class="price-value">650$</div></div>
    </div>
  </article>
</main>
</body>
</html>
```